High quality childcare centre needs a roadside banner

We need a banner designed that advertises our achievement of being rated Exceeding National Quality Standard. Which is the highest rating you can be award as part of the assessment and rating process.

Attached pdf is purely an example although the text as it stands needs to be incorporated.

Please see below for the corporate colors:

Magenta
C-0 M-100 Y-33 K-10
bf00bf

Green
C-78 M-0 Y-100 K-0
00bf00

Target Market(s)

Parents of young children that need childcare

Industry/Entity Type

Childcare

Font styles to use
Sans Serif

Requirements
Must have
• As it is a roadside banner the text should be big, bold and easy to read therefore do not use serif fonts
• Please change found to find
• Logo - see attached
• Supplied wording - see attached
• The specs for the banner are 4m x 1.25m or 4000mm x 1250mm
• The files need to be in the following format:
• jpg, eps and ai.
• Bleeds if relevant
Nice to have
• Other marketing road signs incorporate the attached 'grobold' font
• We also have a motto - 'out of little things, big things grow'
Should not have
• Serif fonts

```html
<!DOCTYPE html>
<html lang="en">
<head>
<meta charset="utf-8">
<title>Tiny Sprouts – Exceeding National Quality Standard Banner</title>
<link rel="stylesheet" href="https://fonts.googleapis.com/css2?family=Lilita+One&display=swap">
<style>
  :root {
    --magenta: #b83fdc;
    --green: #6ee81a;
    --white: #ffffff;
    --paper: #ffffff;
    --photo-skin: #f3c9a8;
    --photo-toy: #9a7be0;
    --photo-kids-a: #f2a35a;
    --photo-kids-b: #5fa8e6;
    --photo-hands-a: #f4c19c;
    --photo-hands-b: #e85a8c;
  }
  * { box-sizing: border-box; margin: 0; padding: 0; }
  html, body {
    width: 1200px;
    height: 457px;
    overflow: hidden;
    background: var(--paper);
  }
  .banner {
    position: relative;
    width: 1200px;
    height: 457px;
    background: var(--paper);
    font-family: "Lilita One", "Arial Rounded MT Bold", sans-serif;
    color: var(--white);
  }
  .bar {
    position: absolute;
    display: flex;
    align-items: center;
    white-space: nowrap;
    line-height: 1;
  }
  .bar--green { background: var(--green); }
  .bar--magenta { background: var(--magenta); }

  .rated-intro {
    left: 249px; top: 40px; width: 434px; height: 59px;
    justify-content: center;
    font-size: 38px;
    padding-left: 40px;
  }
  .rating-line-1 {
    left: 302px; top: 106px; width: 595px; height: 82px;
    justify-content: center;
    font-size: 70px;
  }
  .rating-line-2 {
    left: 364px; top: 196px; width: 595px; height: 77px;
    justify-content: center;
    font-size: 70px;
  }
  .invite {
    left: 614px; top: 278px; width: 542px; height: 56px;
    justify-content: flex-end;
    padding-right: 18px;
    font-size: 38px;
  }
  .motto-bar {
    left: 45px; top: 340px; width: 1111px; height: 69px;
    padding-left: 286px;
    font-size: 37px;
    font-style: oblique 10deg;
  }

  .brand {
    position: absolute;
    left: 70px; top: 60px; width: 206px;
    text-align: center;
    color: var(--green);
  }
  .brand__mark {
    width: 62px; height: 62px;
    margin: 0 auto 8px;
    border-radius: 50%;
    background: var(--magenta);
  }
  .brand__name {
    font-size: 31px;
    line-height: 1;
  }
  .brand__tagline {
    margin-top: 4px;
    font-size: 10.5px;
    line-height: 1;
  }

  .arch {
    position: absolute;
    left: 80px; top: 236px;
    width: 244px; height: 106px;
  }
  .photo {
    position: absolute;
  }
  .photo--child {
    left: 96px; top: 252px; width: 210px; height: 152px;
    border-radius: 100px 100px 6px 6px;
    background: linear-gradient(90deg, var(--photo-skin) 0%, #f6e8df 45%, var(--photo-toy) 70%, #6fc7e8 100%);
  }
  .photo--kids {
    left: 293px; top: 270px; width: 322px; height: 78px;
    border-radius: 30px 30px 4px 4px;
    background: linear-gradient(90deg, var(--photo-kids-a), #e86a9a 35%, var(--photo-kids-b) 65%, #f0c060);
  }
  .photo--hands {
    left: 1050px; top: 42px; width: 106px; height: 226px;
    border-radius: 20px;
    background: linear-gradient(180deg, var(--photo-hands-b), #f2c94c 40%, #5ec46a 70%, var(--photo-hands-a));
  }
</style>
</head>
<body>
<main class="banner">

  <div class="brand">
    <div class="brand__mark"></div>
    <div class="brand__name">Tiny Sprouts</div>
    <div class="brand__tagline">Early Growth &amp; Learning Centre</div>
  </div>

  <div class="bar bar--green rated-intro">This service is rated</div>
  <div class="bar bar--magenta rating-line-1">‘Exceeding National</div>
  <div class="bar bar--magenta rating-line-2">Quality Standard’</div>
  <div class="bar bar--green invite">Come in and out why ......</div>
  <div class="bar bar--magenta motto-bar">'out of little things, big things grow'</div>

  <svg class="arch" viewBox="0 0 244 106" aria-hidden="true">
    <path d="M0 106 A122 104 0 0 1 244 106 L224 106 A102 86 0 0 0 20 106 Z" fill="var(--magenta)"/>
  </svg>

  <div class="photo photo--child" role="img" aria-label="Photo of a smiling toddler building a house from colourful magnetic tiles"></div>
  <div class="photo photo--kids" role="img" aria-label="Photo of a row of smiling children lying on their fronts"></div>
  <div class="photo photo--hands" role="img" aria-label="Photo of children's hands painted in bright colours with smiley faces"></div>

</main>
</body>
</html>
```